Labeling for Organic Food

we need a label design for

1. Organic Red Rice
2. Organic wild honey

it is going to be the same design in different dimensions.

1. Organic Red Rice
Dimension 1 28*18.5cm
Dimension 2 13.5*8cm

2. Organic Honey
12*6cm
Updates

Project Deadline Extended Reason: I still haven't found the right design. Added Monday, June 26, 2017

There is an update in the brief about using the Bhutanese color scheme. Please check it out.

Target Market(s)

people with the concern of health and the environment.

Requirements
Must have
• 1. our logo
• 2. All the info
• 3. A natural feel
• 4. I would prefer minimalistic style
• 5. Please include Bhutanese national colours as attached.

```html
<!DOCTYPE html>
<html lang="en">
<head>
<meta charset="utf-8">
<title>Verdanta Organic Wild Honey Labels</title>
<link rel="stylesheet" href="https://fonts.googleapis.com/css2?family=Bebas+Neue&family=Noto+Sans+SC:wght@300&display=swap">
<style>
  :root {
    --canvas: #efefef;
    --purple-fill: #a47cb6;
    --purple-band: #7f4f94;
    --purple-ink: #5b2c72;
    --yellow-fill: #eee84c;
    --red-band: #b3202a;
    --bhutan-red: #d8262b;
    --bhutan-green: #3aa935;
    --bhutan-yellow: #f2d233;
    --orange-fill: #c2561d;
    --orange-band: #a94513;
    --ink: #161616;
    --white: #ffffff;
  }
  html, body {
    margin: 0;
    width: 1200px;
    height: 800px;
    overflow: hidden;
    background: var(--canvas);
  }
  .label-set {
    width: 1200px;
    height: 800px;
    display: flex;
    align-items: center;
    justify-content: center;
    gap: 40px;
  }
  .label { display: block; }
  .label--side { width: 300px; height: 282px; }
  .label--main { width: 350px; height: 329px; }
  .label text { text-anchor: middle; }
  .brand { font-family: "Bebas Neue", sans-serif; font-size: 40px; letter-spacing: 1px; }
  .title { font-family: "Bebas Neue", sans-serif; font-size: 42px; }
  .title-cn { font-family: "Noto Sans SC", sans-serif; font-weight: 300; font-size: 30px; }
  .origin { font-family: "Bebas Neue", sans-serif; font-size: 24px; }
  .weight { font-family: "Bebas Neue", sans-serif; font-size: 19px; }
</style>
</head>
<body>
<main class="label-set">

  <svg class="label label--side" viewBox="0 0 340 320" aria-label="Organic wild honey label, purple">
    <rect class="band" x="0" y="90" width="340" height="140" fill="var(--purple-band)"/>
    <polygon points="8,160 85,8 255,8 332,160 255,312 85,312" fill="var(--purple-fill)" stroke="var(--purple-band)" stroke-width="3"/>
    <polygon points="20,160 92,20 248,20 320,160 248,300 92,300" fill="none" stroke="var(--white)" stroke-width="3"/>
    <text class="brand" x="170" y="96" fill="var(--white)">Verdanta</text>
    <text class="title" x="170" y="150" fill="var(--purple-ink)">ORGANIC WILD HONEY</text>
    <text class="title-cn" x="170" y="190" fill="var(--white)">有机野生蜂蜜</text>
    <text class="origin" x="170" y="242" fill="var(--white)">PRODUCT OF BHUTAN</text>
    <text class="weight" x="170" y="280" fill="var(--white)">NET WEIGHT 250ML</text>
  </svg>

  <svg class="label label--main" viewBox="0 0 340 320" aria-label="Organic wild honey label, yellow">
    <rect class="band" x="0" y="90" width="340" height="140" fill="var(--red-band)"/>
    <polygon points="8,160 85,8 255,8 332,160 255,312 85,312" fill="var(--yellow-fill)" stroke="var(--bhutan-red)" stroke-width="4"/>
    <polygon points="16,160 89,16 251,16 324,160 251,304 89,304" fill="none" stroke="var(--bhutan-green)" stroke-width="3"/>
    <polygon points="23,160 93,23 247,23 317,160 247,297 93,297" fill="none" stroke="var(--bhutan-red)" stroke-width="2"/>
    <text class="brand" x="170" y="96" fill="var(--ink)">Verdanta</text>
    <text class="title" x="170" y="150" fill="var(--ink)">ORGANIC WILD HONEY</text>
    <text class="title-cn" x="170" y="190" fill="var(--ink)">有机野生蜂蜜</text>
    <text class="origin" x="170" y="242" fill="var(--ink)">PRODUCT OF BHUTAN</text>
    <text class="weight" x="170" y="280" fill="var(--ink)">NET WEIGHT 250ML</text>
  </svg>

  <svg class="label label--side" viewBox="0 0 340 320" aria-label="Organic wild honey label, orange">
    <rect class="band" x="0" y="90" width="340" height="140" fill="var(--orange-band)"/>
    <polygon points="8,160 85,8 255,8 332,160 255,312 85,312" fill="var(--orange-fill)" stroke="var(--bhutan-red)" stroke-width="4"/>
    <polygon points="16,160 89,16 251,16 324,160 251,304 89,304" fill="none" stroke="var(--bhutan-green)" stroke-width="3"/>
    <polygon points="23,160 93,23 247,23 317,160 247,297 93,297" fill="none" stroke="var(--bhutan-yellow)" stroke-width="2"/>
    <text class="brand" x="170" y="96" fill="var(--white)">Verdanta</text>
    <text class="title" x="170" y="150" fill="var(--bhutan-yellow)">ORGANIC WILD HONEY</text>
    <text class="title-cn" x="170" y="190" fill="var(--bhutan-yellow)">有机野生蜂蜜</text>
    <text class="origin" x="170" y="242" fill="var(--bhutan-yellow)">PRODUCT OF BHUTAN</text>
    <text class="weight" x="170" y="280" fill="var(--bhutan-yellow)">NET WEIGHT 250ML</text>
  </svg>

</main>
</body>
</html>
```